Business Card Design Project

Use our current logo. Clean design.

Industry/Entity Type

Business

Requirements
Must have
• Marisela DUCRANTE
M. Law
Managing Partner

Velotrana AG
Brunnmattweg 274
CH-3097 Liebefeld

M. +41 79 418 26 97
T. +41 31 742 19 04
F. +41 31 742 19 38

m.ducrante@velotrana.example
www.velotrana.example

```html
<!DOCTYPE html>
<html lang="en">
<head>
<meta charset="utf-8">
<title>Velotrana AG – Business Card</title>
<link rel="stylesheet" href="https://fonts.googleapis.com/css2?family=Crimson+Text:wght@400&display=swap">
<style>
  :root {
    --backdrop: #3d2619;
    --card-edge: #434446;
    --card-glow: #5e5f61;
    --back-edge: #37383a;
    --back-glow: #4c4d4f;
    --panel: #606162;
    --ink: #f4f4f4;
    --ink-soft: #e2e2e2;
  }
  * { margin: 0; padding: 0; box-sizing: border-box; }
  html, body { width: 936px; height: 1200px; overflow: hidden; }
  body {
    background: var(--backdrop);
    font-family: "Crimson Text", Georgia, serif;
    color: var(--ink);
    position: relative;
  }
  .card {
    position: absolute;
    left: 177px;
    width: 593px;
    height: 341px;
    box-shadow: 0 4px 14px rgba(0,0,0,0.45);
  }
  .card--front {
    top: 227px;
    background: radial-gradient(ellipse at 50% 55%, var(--card-glow) 0%, var(--card-edge) 75%);
    display: flex;
    align-items: center;
    justify-content: center;
  }
  .brand-name {
    font-size: 32px;
    letter-spacing: 3px;
    text-transform: uppercase;
    color: var(--ink);
  }
  .card--back {
    top: 624px;
    background: radial-gradient(ellipse at 50% 60%, var(--back-glow) 0%, var(--back-edge) 70%);
  }
  .info-panel {
    position: absolute;
    top: 115px;
    height: 110px;
    background: var(--panel);
    font-size: 10px;
    line-height: 12.5px;
    color: var(--ink-soft);
    text-align: center;
    padding-top: 36px;
  }
  .info-panel--address { left: 0; width: 190px; border-radius: 0 5px 5px 0; }
  .info-panel--phone { right: 0; width: 185px; border-radius: 5px 0 0 5px; }
  .holder {
    position: absolute;
    left: 190px;
    right: 185px;
    top: 120px;
    text-align: center;
  }
  .holder__name { font-size: 18px; letter-spacing: 0.5px; color: var(--ink); }
  .holder__role { margin-top: 11px; font-size: 11px; line-height: 13px; color: var(--ink-soft); }
  .holder__web { margin-top: 12px; font-size: 10.5px; line-height: 12.5px; color: var(--ink-soft); }
</style>
</head>
<body>
  <section class="card card--front">
    <span class="brand-name">Velotrana</span>
  </section>

  <section class="card card--back">
    <div class="info-panel info-panel--address">
      Velotrana AG<br>
      Brunnmattweg 274<br>
      CH-3097 Liebefeld
    </div>

    <div class="holder">
      <p class="holder__name">Marisela DUCRANTE</p>
      <p class="holder__role">M. Law<br>Managing Partner</p>
      <p class="holder__web">m.ducrante@velotrana.example<br>www.velotrana.example</p>
    </div>

    <div class="info-panel info-panel--phone">
      M. +41 79 418 26 97<br>
      T. +41 31 742 19 04<br>
      F. +41 31 742 19 38
    </div>
  </section>
</body>
</html>
```